Life Saving Rules DOKVE

Design a wallet/business card size document front and back to depict the attached lifesaving rules in the color scheme of the business logo attached. (Also attached is an example of a similar card)

Target Market(s)

End User - Field Employees

Industry/Entity Type

Refining

Requirements
Must have
• All Life Saving rules with graphics, using front and back of card, information needs to flow.
Nice to have
• Would like the design to be similar to the card uploaded but better with graphics

```html
<!DOCTYPE html>
<html lang="en">
<head>
<meta charset="utf-8">
<title>Life Saving Rules – DOKVE</title>
<link href="https://fonts.googleapis.com/css2?family=Montserrat:wght@400;500;600&display=swap" rel="stylesheet">
<style>
  :root {
    --backdrop: #cfcfcf;
    --card: #ffffff;
    --green: #3fbf3a;
    --green-soft: #a9dc98;
    --blue: #1fa3e0;
    --blue-soft: #9fd3f0;
    --ink: #1d1d1d;
    --brand-ink: #4a4a4a;
  }
  * { box-sizing: border-box; margin: 0; padding: 0; }
  html, body { width: 852px; height: 1200px; overflow: hidden; }
  body {
    background: var(--backdrop);
    font-family: "Montserrat", sans-serif;
    color: var(--ink);
    position: relative;
  }
  .card {
    position: absolute;
    left: 148px;
    width: 556px;
    height: 318px;
    background: var(--card);
    border-radius: 14px;
    box-shadow: 0 4px 8px rgba(0,0,0,0.25);
    overflow: hidden;
  }
  .card--front { top: 252px; }
  .card--back { top: 630px; }

  .corner-accent { position: absolute; width: 46px; height: 42px; }
  .corner-accent--tl { top: 0; left: 0; }
  .corner-accent--tr { top: 0; right: 0; transform: scaleX(-1); }
  .corner-accent--bl { bottom: 0; left: 0; transform: scaleY(-1); }
  .corner-accent--br { bottom: 0; right: 0; transform: scale(-1,-1); }

  .brand-name {
    position: absolute;
    top: 56px; left: 0; right: 0;
    text-align: center;
    font-size: 21px;
    font-weight: 600;
    color: var(--brand-ink);
  }
  .card-title {
    position: absolute;
    top: 90px; left: 0; right: 0;
    text-align: center;
    font-size: 35px;
    font-weight: 600;
    color: var(--green);
    letter-spacing: 0.3px;
  }
  .title-rule {
    position: absolute;
    top: 131px; left: 105px;
    width: 346px; height: 1px;
    background: var(--green);
  }

  .rule {
    position: absolute;
    width: 150px;
    margin-left: -75px;
    text-align: center;
  }
  .rule-text {
    font-size: 11.5px;
    font-weight: 500;
    line-height: 13.3px;
    white-space: nowrap;
  }
  .rule-icon { display: block; margin: 0 auto; }
  .rule--front { top: 160px; }
  .rule--front .rule-icon { width: 60px; height: 60px; margin-bottom: 14px; }
  .rule--back .rule-icon { width: 50px; height: 50px; margin-bottom: 6px; }
  .rule--row1 { top: 36px; }
  .rule--row2 { top: 172px; }
</style>
</head>
<body>

<section class="card card--front" aria-label="Life saving rules, front">
  <svg class="corner-accent corner-accent--tl" viewBox="0 0 46 42" role="img" aria-label="Leaf corner ornament"><defs><linearGradient id="leafA" x1="0" y1="0" x2="1" y2="1"><stop offset="0" stop-color="var(--blue-soft)"/><stop offset="0.5" stop-color="var(--green-soft)"/></linearGradient></defs><polygon points="0,0 46,0 0,42" fill="url(#leafA)"/></svg>
  <svg class="corner-accent corner-accent--tr" viewBox="0 0 46 42" role="img" aria-label="Leaf corner ornament"><polygon points="0,0 46,0 0,42" fill="url(#leafA)"/></svg>

  <div class="brand-name">DOKVE</div>
  <h1 class="card-title">LIFE SAVING RULES</h1>
  <div class="title-rule"></div>

  <div class="rule rule--front" style="left:75px">
    <svg class="rule-icon" viewBox="0 0 60 60" role="img" aria-label="No smoking sign">
      <rect x="13" y="32" width="30" height="6" fill="var(--blue)"/>
      <rect x="39" y="32" width="4" height="6" fill="#fff"/>
      <path d="M38 29c-3-4 3-6 0-10s3-5 0-9M43 29c-3-4 3-6 0-10" fill="none" stroke="var(--blue)" stroke-width="2"/>
      <circle cx="30" cy="30" r="26" fill="none" stroke="var(--blue)" stroke-width="4.5"/>
      <line x1="12" y1="12" x2="48" y2="48" stroke="var(--blue)" stroke-width="4.5"/>
    </svg>
    <p class="rule-text">Do not smoke<br>outside of<br>designated smoking<br>areas</p>
  </div>
  <div class="rule rule--front" style="left:211px">
    <svg class="rule-icon" viewBox="0 0 60 60" role="img" aria-label="No alcohol or drugs sign">
      <path d="M27 10h6v10l5 7v21H22V27l5-7z" fill="var(--blue)"/>
      <circle cx="30" cy="30" r="26" fill="none" stroke="var(--blue)" stroke-width="4.5"/>
      <line x1="48" y1="12" x2="12" y2="48" stroke="#fff" stroke-width="8"/>
      <line x1="48" y1="12" x2="12" y2="48" stroke="var(--blue)" stroke-width="4.5"/>
    </svg>
    <p class="rule-text">No alcohol or<br>drugs while working<br>or driving</p>
  </div>
  <div class="rule rule--front" style="left:343px">
    <svg class="rule-icon" viewBox="0 0 60 60" role="img" aria-label="No walking under suspended loads sign">
      <circle cx="31" cy="14" r="3.5" fill="var(--blue)"/>
      <path d="M28 19h6l2 12-3 2 3 12h-4l-3-10-3 10h-4l4-14-2-4-3 5-3-2z" fill="var(--blue)"/>
      <circle cx="30" cy="30" r="26" fill="none" stroke="var(--blue)" stroke-width="4.5"/>
      <line x1="12" y1="12" x2="48" y2="48" stroke="#fff" stroke-width="8"/>
      <line x1="12" y1="12" x2="48" y2="48" stroke="var(--blue)" stroke-width="4.5"/>
    </svg>
    <p class="rule-text">Do not walk<br>under suspended<br>loads</p>
  </div>
  <div class="rule rule--front" style="left:475px">
    <svg class="rule-icon" viewBox="0 0 60 60" role="img" aria-label="No phone use while driving sign">
      <rect x="21" y="13" width="18" height="33" rx="3" fill="none" stroke="var(--blue)" stroke-width="3"/>
      <line x1="27" y1="41" x2="33" y2="41" stroke="var(--blue)" stroke-width="2"/>
      <circle cx="30" cy="30" r="26" fill="none" stroke="var(--blue)" stroke-width="4.5"/>
      <line x1="12" y1="12" x2="48" y2="48" stroke="#fff" stroke-width="8"/>
      <line x1="12" y1="12" x2="48" y2="48" stroke="var(--blue)" stroke-width="4.5"/>
    </svg>
    <p class="rule-text">while driving, do<br>not use your phone<br>and do not exceed<br>speed limits</p>
  </div>
</section>

<section class="card card--back" aria-label="Life saving rules, back">
  <svg class="corner-accent corner-accent--bl" viewBox="0 0 46 42" role="img" aria-label="Leaf corner ornament"><polygon points="0,0 46,0 0,42" fill="url(#leafA)"/></svg>
  <svg class="corner-accent corner-accent--br" viewBox="0 0 46 42" role="img" aria-label="Leaf corner ornament"><polygon points="0,0 46,0 0,42" fill="url(#leafA)"/></svg>

  <div class="rule rule--back rule--row1" style="left:82px">
    <svg class="rule-icon" viewBox="0 0 50 50" role="img" aria-label="Locked safety control icon">
      <path d="M20 2l18 7v12c0 12-8 20-18 24C10 41 2 33 2 21V9z" fill="var(--green)"/>
      <rect x="13" y="18" width="14" height="11" rx="1.5" fill="#fff"/>
      <path d="M15.5 18v-4a4.5 4.5 0 0 1 9 0v4" fill="none" stroke="#fff" stroke-width="2.2"/>
      <circle cx="36" cy="36" r="12" fill="var(--green)" stroke="#fff" stroke-width="2"/>
      <circle cx="36" cy="32" r="3.5" fill="#fff"/>
      <path d="M29 42a7 6 0 0 1 14 0z" fill="#fff"/>
    </svg>
    <p class="rule-text">Obtain authorisation<br>before overriding or<br>disabling safety controls</p>
  </div>
  <div class="rule rule--back rule--row1" style="left:224px">
    <svg class="rule-icon" viewBox="0 0 50 50" role="img" aria-label="Worker in confined space icon">
      <circle cx="25" cy="6" r="5" fill="var(--green)"/>
      <rect x="18" y="13" width="14" height="18" rx="3" fill="var(--green)"/>
      <ellipse cx="25" cy="40" rx="22" ry="8" fill="var(--green)"/>
      <rect x="20" y="30" width="4" height="10" fill="#fff"/>
      <rect x="26" y="30" width="4" height="10" fill="#fff"/>
    </svg>
    <p class="rule-text">Obtain authorisation<br>before entering a<br>confined space</p>
  </div>
  <div class="rule rule--back rule--row1" style="left:353px">
    <svg class="rule-icon" viewBox="0 0 50 50" role="img" aria-label="Isolated energy source icon">
      <rect x="17" y="1" width="10" height="5" rx="1" fill="var(--green)"/>
      <rect x="11" y="5" width="22" height="42" rx="4" fill="var(--green)"/>
      <path d="M23 14l-6 12h5l-3 10 8-14h-5l3-8z" fill="#fff"/>
      <circle cx="36" cy="34" r="10" fill="var(--green)" stroke="#fff" stroke-width="2"/>
      <circle cx="36" cy="34" r="5.5" fill="none" stroke="#fff" stroke-width="2"/>
      <line x1="32" y1="38" x2="40" y2="30" stroke="#fff" stroke-width="2"/>
    </svg>
    <p class="rule-text">Verify isolation and<br>zero energy before<br>work begins</p>
  </div>
  <div class="rule rule--back rule--row1" style="left:484px">
    <svg class="rule-icon" viewBox="0 0 50 50" role="img" aria-label="Flame and ignition source icon">
      <path d="M25 2c2 8 12 12 12 22a12 12 0 0 1-24 0c0-6 4-8 5-13 2 3 2 6 4 7 2-5 3-10 3-16z" fill="var(--green)"/>
      <path d="M25 22c1 4 5 6 5 10a5 5 0 0 1-10 0c0-4 4-5 5-10z" fill="#fff"/>
      <line x1="5" y1="38" x2="45" y2="46" stroke="var(--green)" stroke-width="4.5" stroke-linecap="round"/>
      <line x1="5" y1="46" x2="45" y2="38" stroke="var(--green)" stroke-width="4.5" stroke-linecap="round"/>
    </svg>
    <p class="rule-text">Control frammables<br>and ignition sources</p>
  </div>

  <div class="rule rule--back rule--row2" style="left:136px">
    <svg class="rule-icon" viewBox="0 0 50 50" role="img" aria-label="Crane lifting a load icon">
      <line x1="8" y1="6" x2="40" y2="14" stroke="var(--green)" stroke-width="3"/>
      <line x1="10" y1="7" x2="10" y2="24" stroke="var(--green)" stroke-width="1.5"/>
      <rect x="4" y="24" width="12" height="14" rx="1" fill="var(--green)"/>
      <line x1="40" y1="14" x2="34" y2="30" stroke="var(--green)" stroke-width="3"/>
      <path d="M20 30h16l4-6h6v16H20z" fill="var(--green)"/>
      <circle cx="26" cy="41" r="4" fill="var(--green)" stroke="#fff" stroke-width="1.5"/>
      <circle cx="40" cy="41" r="4" fill="var(--green)" stroke="#fff" stroke-width="1.5"/>
    </svg>
    <p class="rule-text">Plan lifting operations<br>and control the area</p>
  </div>
  <div class="rule rule--back rule--row2" style="left:278px">
    <svg class="rule-icon" viewBox="0 0 50 50" role="img" aria-label="Work permit document icon">
      <path d="M6 2h24l8 8v38H6z" fill="var(--green)"/>
      <circle cx="16" cy="13" r="4" fill="#fff"/>
      <path d="M10 24a6 5 0 0 1 12 0z" fill="#fff"/>
      <rect x="10" y="29" width="18" height="2.5" fill="#fff"/>
      <rect x="10" y="35" width="14" height="2.5" fill="#fff"/>
      <path d="M36 26l10 4v7c0 6-4 10-10 12-6-2-10-6-10-12v-7z" fill="var(--green)" stroke="#fff" stroke-width="2"/>
      <path d="M31 37l4 4 6-7" fill="none" stroke="#fff" stroke-width="2.2"/>
    </svg>
    <p class="rule-text">Work with a valid<br>permit when required</p>
  </div>
  <div class="rule rule--back rule--row2" style="left:420px">
    <svg class="rule-icon" viewBox="0 0 50 50" role="img" aria-label="Worker with fall protection icon">
      <line x1="30" y1="1" x2="24" y2="16" stroke="var(--green)" stroke-width="2"/>
      <circle cx="22" cy="18" r="4" fill="var(--green)"/>
      <path d="M19 22l6 2-2 10 5 8-3 2-6-8-4 6-3-2 5-8z" fill="var(--green)"/>
      <line x1="20" y1="24" x2="12" y2="20" stroke="var(--green)" stroke-width="2.5"/>
      <path d="M37 32l8 3v5c0 5-3 7-8 9-5-2-8-4-8-9v-5z" fill="var(--green)"/>
      <path d="M33 40l3 3 5-6" fill="none" stroke="#fff" stroke-width="2"/>
    </svg>
    <p class="rule-text">Protect yourself<br>against a fall when<br>working at height</p>
  </div>
</section>

</body>
</html>
```